Website for The Copper Lantern

We need an impressive e-commerce website for our newly launched business "The Copper Lantern".
The Copper Lantern searches store-front and online retailers for diamond engagement rings according to the client's specified requirements. We want to save people time by doing the shopping around for them.
We can relate to, and we love, www.roomtrellis.com
Like roomtrellis.com, we want to offer website visitors a quick run-down on how the process works, then offer them to elect a service package and pay for that package on the spot.
Content pages:
HOME
HOW IT WORKS
DIAMOND GALLERY
ABOUT
FAQs
CONTACT
Inclusions: Our logo and Facebook and Instagram buttons
We want to be able to easily edit this website, We want it to display well on iPhone and android, We want it to be clean and striking.
Like our logo, we want our website to embody elegant masculinity.
Target Market(s)
Men in market for diamond ring purchase $5k - $50k
Industry/Entity Type
Business
Number of Pages Required
5+ page
Font styles to use
Look and feel

```html
<!DOCTYPE html>
<html lang="en">
<head>
<meta charset="utf-8">
<title>The Copper Lantern — Find Your Perfect Diamond</title>
<link rel="stylesheet" href="https://fonts.googleapis.com/css2?family=Cinzel:wght@400;700&family=Noto+Serif:ital@0;1&family=Montserrat:wght@500;700&family=Roboto+Slab:wght@400;700&display=swap">
<style>
:root{
  --bg-top:#f7f7f7;
  --bg-main:#ffffff;
  --ink:#7a7a7a;
  --ink-soft:#8a8a8a;
  --ink-dark:#6a6a6a;
  --rule:#9a9a9a;
  --card-bg:#fafafa;
  --card-border:#e2e2e2;
  --photo-ring:#e4e4e4;
  --photo-faint:#f6f6f6;
}
*{margin:0;padding:0;box-sizing:border-box}
html,body{width:1200px;height:1000px;overflow:hidden;background:var(--bg-main)}
body{position:relative;font-family:"Noto Serif",serif;color:var(--ink)}
.process{position:absolute;left:0;top:0;width:1200px;height:442px;background:var(--bg-top)}
.hero-ring{position:absolute;left:30px;top:85px;width:270px;height:310px;border-radius:40%;
  background:radial-gradient(ellipse at 45% 40%,#fdfdfd 0%,var(--photo-ring) 55%,var(--bg-top) 75%)}
.process-title{position:absolute;left:370px;top:50px;width:693px;display:flex;align-items:center;gap:8px;
  font-family:"Cinzel",serif;font-size:34px;color:var(--ink);white-space:nowrap}
.process-title::before,.process-title::after{content:"";flex:1;height:1.5px;background:var(--rule)}
.process-title .lead{font-style:italic;font-weight:400}
.process-title strong{font-weight:700;font-style:italic}
.process-intro{position:absolute;left:340px;top:105px;width:760px;text-align:center;
  font-style:italic;font-size:20px;line-height:27px;color:var(--ink-soft)}
.step{position:absolute;top:196px;width:190px;text-align:center}
.step svg{display:block;margin:0 auto;width:90px;height:86px}
.step p{margin-top:8px;font-style:italic;font-size:18px;line-height:24px;color:var(--ink-soft)}
.step-1{left:305px}.step-2{left:523px}.step-3{left:743px}.step-4{left:965px}
.packages{position:absolute;left:0;top:442px;width:1200px;height:500px}
.backdrop-ring{position:absolute;left:120px;top:48px;width:1080px;height:438px;
  background:linear-gradient(90deg,#fdfdfd 0%,var(--photo-faint) 55%,#f1f1f1 80%,#fbfbfb 100%)}
.plan{position:absolute;top:67px;width:233px;height:349px;background:var(--card-bg);
  border:1.5px solid var(--card-border);border-radius:10px;text-align:center}
.plan-1{left:50px}.plan-2{left:312px}.plan-3{left:575px}
.plan h3{margin-top:38px;font-family:"Cinzel",serif;font-weight:400;font-size:19px;letter-spacing:1px;color:var(--ink-dark)}
.price{margin-top:18px;display:flex;justify-content:center;align-items:flex-end;font-family:"Montserrat",sans-serif;color:var(--ink)}
.price .cur{font-size:18px;align-self:flex-start;margin-top:8px;margin-right:6px}
.price .amt{font-size:76px;font-weight:700;line-height:76px;letter-spacing:-1px}
.price .per{font-size:18px;font-weight:500;margin-left:2px;margin-bottom:4px}
.plan ul{list-style:none;margin-top:30px;font-size:19px;line-height:30.5px;color:var(--ink-soft)}
.collection{position:absolute;left:0;top:942px;width:1200px;height:58px;font-family:"Roboto Slab",serif}
.collection h2{position:absolute;left:34px;top:14px;font-size:24px;font-weight:700;color:var(--ink)}
.collection nav{position:absolute;right:54px;top:20px;display:flex;gap:35px;font-size:15px;color:var(--ink-soft)}
</style>
</head>
<body>
<section class="process">
  <div class="hero-ring" role="img" aria-label="Photo of a diamond solitaire engagement ring with pavé band"></div>
  <h1 class="process-title"><span><span class="lead">Find your</span> <strong>PERFECT DIAMOND</strong></span></h1>
  <p class="process-intro">Choosing your diamond is an exciting process. Carat, cut, clarity, and colour our handy process makes it easier for you to find your perfect combination.</p>

  <div class="step step-1">
    <svg viewBox="0 0 90 86" fill="none" stroke="#888" stroke-width="4">
      <circle cx="38" cy="38" r="34"/><ellipse cx="38" cy="38" rx="14" ry="34"/>
      <line x1="4" y1="38" x2="72" y2="38"/><path d="M10 20h56M10 56h56"/>
      <circle cx="56" cy="56" r="13" fill="#f7f7f7"/><line x1="65" y1="65" x2="78" y2="78" stroke-width="7" stroke-linecap="round"/>
    </svg>
    <p>Determine your style with our effortless style survey</p>
  </div>
  <div class="step step-2">
    <svg viewBox="0 0 90 86" fill="none" stroke="#888" stroke-width="4" stroke-linejoin="round">
      <path d="M20 8h50l16 20-41 52L4 28z"/><path d="M4 28h82M20 8l12 20 13-20 13 20 12-20M32 28l13 52 13-52"/>
    </svg>
    <p>Choose your designer and upload photos.</p>
  </div>
  <div class="step step-3">
    <svg viewBox="0 0 90 86" fill="none" stroke="#888" stroke-width="5" stroke-linejoin="round">
      <path d="M2 12h12l10 46h44l8-30H40"/><circle cx="32" cy="72" r="5"/><circle cx="60" cy="72" r="5"/>
      <circle cx="66" cy="24" r="19" fill="#f7f7f7"/><path d="M66 13v18M58 24l8 8 8-8"/>
    </svg>
    <p>Work with your designer online to get your design ideas.</p>
  </div>
  <div class="step step-4">
    <svg viewBox="0 0 90 86" fill="none" stroke="#888" stroke-width="3">
      <rect x="17" y="5" width="56" height="76" rx="3"/><rect x="23" y="12" width="44" height="62"/>
      <rect x="35" y="2" width="20" height="8" fill="#f7f7f7"/>
      <path d="M29 20h12M29 28h32M29 36h32M29 44h24M29 52h32M54 64l3 3 6-6"/>
    </svg>
    <p>Order everything at the best prices through our store.</p>
  </div>
</section>

<section class="packages">
  <div class="backdrop-ring" role="img" aria-label="Faint photo of a diamond eternity band and a floral diamond ring"></div>
  <article class="plan plan-1">
    <h3>LANTERN MINI</h3>
    <div class="price"><span class="cur">$</span><span class="amt">18</span><span class="per">/mo</span></div>
    <ul><li>Package Text</li><li>Package Text</li><li>Package Text</li></ul>
  </article>
  <article class="plan plan-2">
    <h3>LANTERN PRO</h3>
    <div class="price"><span class="cur">$</span><span class="amt">24</span><span class="per">/mo</span></div>
    <ul><li>Package Text</li><li>Package Text</li><li>Package Text</li><li>Package Text</li></ul>
  </article>
  <article class="plan plan-3">
    <h3>LANTERN CHIEF</h3>
    <div class="price"><span class="cur">$</span><span class="amt">32</span><span class="per">/mo</span></div>
    <ul><li>Package Text</li><li>Package Text</li><li>Package Text</li></ul>
  </article>
</section>

<section class="collection">
  <h2>NEW COLLECTION</h2>
  <nav><span>ALL</span><span>MEN</span><span>WOMEN</span><span>SHOP</span><span>ACCESSORIES</span></nav>
</section>
</body>
</html>
```